Business card design for immigration consulting business

We need business card design for a company called T&R Migration Advisors Inc. This is a boutique immigration consulting and foreign recruitment agency owned and managed by two partners.
The business card will be used by partners \ owners of the business. The best way to describe the business would be committed to client, passionate about providing top-notch services, engaging, competent, professional

Target Market(s)

We work with individuals in and outside of Canada who need immigration advise as well as Canadian businesses looking to hire or sponsor foreign workers to Canada

Industry/Entity Type

Consulting

Contact Information for Business Card

The business card should have a standard size and horizontal lay-out

Font styles to use
Serif

Colors
f04a50
ec1f27
cbcbcb
dbdbdb

Requirements
Must have
• The business card mush have our logo, name of the company first and last name of the partner, position, phone, cell, fax, e-mail, skype, web-site
• Our first choice would a classic design with minimalist looks and elegant fonts and colors, but we are open minded to any creative ideas too
Nice to have
• On the other side it may have the description of the company: Immigration and Foreign Recruitment Services
• We're considering using stamping \ lettering on our business cards
• It would be nice if the business card would have white space, in case someone would like to make notes on it.
• One (back side) side of the business card can be all red with white logo
Should not have
• We do not want to have our pictures on the business card
• We do no want to have Canadian maple leaf on the business card as we already have one in our logo

```html
<!DOCTYPE html>
<html lang="en">
<head>
<meta charset="utf-8">
<title>T&amp;R Migration Advisors Inc. — Business Card</title>
<link rel="stylesheet" href="https://fonts.googleapis.com/css2?family=Open+Sans:wght@400;600&display=swap">
<style>
  :root {
    --backdrop: #3a3a3a;
    --card-black: #1f1f20;
    --card-white: #f2f2f2;
    --red: #ec1f27;
    --red-soft: #f04a50;
    --grey-light: #dbdbdb;
    --grey-mid: #cbcbcb;
    --ink: #4a4a4a;
    --ink-dark: #3c3c3c;
    --silver: #9a9a9a;
  }
  * { margin: 0; padding: 0; box-sizing: border-box; }
  html, body {
    width: 799px; height: 1200px; overflow: hidden;
    background: var(--backdrop);
    font-family: "Open Sans", Arial, sans-serif;
  }
  .canvas {
    position: relative; width: 799px; height: 1200px;
    display: flex; flex-direction: column; align-items: center; justify-content: space-around;
    padding: 60px 0;
  }
  .card {
    position: relative; width: 640px; height: 366px;
    border-radius: 26px; overflow: hidden;
  }
  /* Front */
  .card-front { background: var(--card-black); display: flex; align-items: center; justify-content: center; }
  .front-mark {
    display: flex; align-items: center; gap: 14px;
    color: var(--silver); font-weight: 600; font-size: 26px; letter-spacing: 1px;
  }
  .front-mark .dot { width: 18px; height: 18px; border-radius: 50%; background: var(--silver); }
  /* Back */
  .card-back { background: var(--card-white); }
  .web-band {
    position: absolute; right: 0; bottom: 0; width: 70%; height: 46px;
    background: var(--red); border-top-left-radius: 30px;
    display: flex; align-items: center; padding-left: 70px;
    color: #fff; font-size: 18px;
  }
  .brand {
    position: absolute; left: 44px; top: 92px;
    display: flex; align-items: center; gap: 12px;
    color: var(--ink); font-weight: 600; font-size: 25px; letter-spacing: .5px; line-height: 1.2;
  }
  .brand .square { width: 14px; height: 14px; background: var(--red); flex: none; }
  .person { position: absolute; left: 330px; top: 108px; }
  .person-name { color: var(--red); font-weight: 600; font-size: 23px; line-height: 1.15; }
  .person-role { color: var(--ink); font-size: 14px; margin-top: 2px; }
  .contacts { list-style: none; margin-top: 10px; }
  .contacts li {
    display: flex; align-items: center; gap: 9px;
    color: var(--ink-dark); font-size: 15px; line-height: 22px;
  }
  .contacts svg { width: 13px; height: 13px; fill: var(--red); flex: none; }
</style>
</head>
<body>
<main class="canvas">
  <section class="card card-front" aria-label="Card front">
    <div class="front-mark"><span class="dot"></span><span>T&amp;R Migration Advisors Inc.</span></div>
  </section>

  <section class="card card-back" aria-label="Card back">
    <div class="brand"><span class="square"></span><span>T&amp;R Migration<br>Advisors Inc.</span></div>

    <div class="person">
      <p class="person-name">Daniel Reeve Carter</p>
      <p class="person-role">Partner / Owner</p>
      <ul class="contacts">
        <li><svg viewBox="0 0 16 16"><circle cx="8" cy="8" r="7"/></svg>DanielCarter</li>
        <li><svg viewBox="0 0 16 16"><path d="M3 1h3l1 4-2 1a9 9 0 0 0 5 5l1-2 4 1v3c0 1-1 2-2 2C7 15 1 9 1 3c0-1 1-2 2-2z"/></svg>416-555-0142</li>
        <li><svg viewBox="0 0 16 16"><path d="M4 0h8a1 1 0 0 1 1 1v14a1 1 0 0 1-1 1H4a1 1 0 0 1-1-1V1a1 1 0 0 1 1-1zm1 2v10h6V2zm3 11a1 1 0 1 0 0 2 1 1 0 0 0 0-2z"/></svg>647-555-0186</li>
        <li><svg viewBox="0 0 16 16"><path d="M4 1h7l2 2v3H4zM1 7h14v6h-2v2H3v-2H1zm4 4v3h6v-3z"/></svg>905-555-0173</li>
        <li><svg viewBox="0 0 16 16"><path d="M1 3h14v10H1zm1 1v.5l6 4 6-4V4z"/></svg>d.carter@tr-migration.com</li>
      </ul>
    </div>

    <div class="web-band">www.tr-migration.com</div>
  </section>
</main>
</body>
</html>
```